Web form face-lift for an online startup

We are a web startup building a SaaS application for the Cargoline Hub. The project is mainly dedicated to the paint the main form that our customer are using along the search results that the they get. All details are in the attached documents.
Updates
The application serves the Freight Forwarders community so please think towards this industry when using background images, banners, colors, icons, etc. Computer and technology images are irrelevant.
Customer fields at the top of the page is actually part of the form.
Target Market(s)
Usually business users (Sales people, procurement, shippers, freight forwarders). Some are less tech savvy and some appreciate the new trendy web apps.
Industry/Entity Type
Building
Colors
Designer to choose colors to be used in the design.
Look and feel
Each slider illustrates characteristics of the customer's brand and the style your logo design should communicate.

```html
<!DOCTYPE html>
<html lang="en">
<head>
<meta charset="utf-8">
<title>Cargoline Hub – Search the Quotes</title>
<link href="https://fonts.googleapis.com/css2?family=Arimo:wght@400;700&family=Tinos:wght@400;700&display=swap" rel="stylesheet">
<style>
:root{
  --bg:#3a97dd;
  --panel:#2f7fc3;
  --panel-edge:#4aa3e4;
  --field:#3a94de;
  --field-edge:#54a9ea;
  --title:#cfe6f8;
  --white:#ffffff;
  --line:#6db6ee;
  --crane:#2f80c6;
  --ground:#2c79bb;
  --tick:#2a7bc4;
}
*{box-sizing:border-box;margin:0;padding:0}
html,body{width:1200px;height:1029px;overflow:hidden;background:var(--bg)}
body{font-family:"Arimo",Arial,sans-serif;color:var(--white);position:relative}
.abs{position:absolute}
.header-line{left:0;top:75px;width:1200px;height:1px;background:var(--line);opacity:.5}
.brand{left:174px;top:16px;font-family:"Tinos","Times New Roman",serif;font-weight:700;font-size:31px;color:var(--white)}
.nav{top:32px;display:flex;font-size:11px;align-items:center}
.nav span{display:flex;align-items:center}
.nav .dot{width:3px;height:3px;border-radius:50%;background:var(--white);margin:0 9px}
.chev{margin-left:3px}
.hero-title{left:0;width:1200px;top:112px;text-align:center;font-family:"Tinos","Times New Roman",serif;font-weight:700;font-size:35px;letter-spacing:.5px;text-shadow:0 0 14px rgba(20,80,150,.5)}
.hero-sub{left:0;width:1200px;top:160px;text-align:center;font-size:16px}
.rule{height:1px;background:linear-gradient(90deg,transparent,var(--line),transparent)}
.panel{background:var(--panel);border:1px solid var(--panel-edge)}
.panel-title{position:absolute;left:0;width:100%;top:12px;text-align:center;font-family:"Tinos","Times New Roman",serif;font-weight:700;font-size:16px;color:var(--title)}
.label{position:absolute;font-size:11px;text-transform:uppercase}
.field{position:absolute;height:36px;background:var(--field);border:1px solid var(--field-edge);font-size:12px;display:flex;align-items:center;padding:0 8px}
.field.center{justify-content:center}
.field .ctl{position:absolute;right:7px;top:50%;transform:translateY(-50%)}
.check{position:absolute;width:18px;height:18px;background:var(--white);border:1px solid #9fcbee}
.check svg{position:absolute;left:1px;top:-3px}
.method{position:absolute;width:64px;height:64px;border-radius:50%;border:3px solid #5db0ec;background:radial-gradient(circle at 50% 40%,#b48e67,#5c4a3c)}
.method.ship{background:linear-gradient(#5ea7e2 0 45%,#c23c2e 45% 62%,#233c66 62%)}
.method.env{background:radial-gradient(circle at 50% 45%,#e0b24a,#6a3a28)}
.method-name{position:absolute;width:90px;text-align:center;font-size:11px;font-weight:700;line-height:12px}
.opt{position:absolute;font-size:11px}
.search-bar{left:171px;top:615px;width:858px;height:62px;display:flex;align-items:center;justify-content:center;font-family:"Tinos","Times New Roman",serif;font-size:19px;color:var(--title);letter-spacing:.5px}
.manual{left:0;width:1200px;top:685px;text-align:center;font-size:13px}
.cranes{left:0;top:760px;width:1200px;height:183px;background:linear-gradient(180deg,rgba(47,128,198,0) 0%,rgba(47,128,198,.75) 25%,var(--crane) 60%,var(--crane) 100%)}
.footer{left:0;top:943px;width:1200px;height:86px;background:var(--ground)}
.copyright{left:174px;top:984px;font-family:"Tinos","Times New Roman",serif;font-size:10px}
.social{top:984px;width:12px;height:12px;border-radius:50%;background:var(--white);opacity:.9}
</style>
</head>
<body>

<div class="abs brand">Cargoline Hub</div>
<nav class="abs nav" style="left:459px">
  <span>HOME</span><span class="dot"></span><span>FREIGHT</span><span class="dot"></span><span>ABOUT</span><span class="dot"></span><span>INDUSTRY</span><span class="dot"></span><span>SERVICES</span><span class="dot" style="margin:0 4px 0 9px"></span><span>CONTACT</span>
</nav>
<nav class="abs nav" style="left:889px">
  <span>LOGIN<svg class="chev" width="8" height="5" viewBox="0 0 8 5"><path d="M1 1l3 3 3-3" stroke="#fff" stroke-width="1.5" fill="none"/></svg></span><span class="dot"></span>
  <span>$<svg class="chev" width="8" height="5" viewBox="0 0 8 5"><path d="M1 1l3 3 3-3" stroke="#fff" stroke-width="1.5" fill="none"/></svg></span><span class="dot"></span>
  <span>EN<svg class="chev" width="8" height="5" viewBox="0 0 8 5"><path d="M1 1l3 3 3-3" stroke="#fff" stroke-width="1.5" fill="none"/></svg></span>
</nav>
<div class="abs header-line"></div>

<div class="abs rule" style="left:180px;top:136px;width:220px"></div>
<div class="abs rule" style="left:800px;top:136px;width:220px"></div>
<h1 class="abs hero-title">SEARCH THE QUOTES !</h1>
<div class="abs rule" style="left:260px;top:170px;width:230px"></div>
<div class="abs rule" style="left:710px;top:170px;width:230px"></div>
<p class="abs hero-sub">Fast And Quick Search !</p>

<section class="abs panel" style="left:171px;top:221px;width:278px;height:180px">
  <h2 class="panel-title">01- SELECT METHOD</h2>
  <div class="method" style="left:19px;top:56px" role="img" aria-label="Warehouse shelves stacked with boxes and pallets"></div>
  <div class="method ship" style="left:107px;top:56px" role="img" aria-label="Container ship at sea"></div>
  <div class="method env" style="left:194px;top:56px" role="img" aria-label="Warehouse aisle with parcels"></div>
  <div class="method-name" style="left:6px;top:130px">Boxes<br>&amp; Pallets</div>
  <div class="method-name" style="left:94px;top:130px">Shipping<br>Countainers</div>
  <div class="method-name" style="left:181px;top:130px">Envelopes<br>&amp; Parcels</div>
</section>

<section class="abs panel" style="left:460px;top:221px;width:569px;height:180px">
  <h2 class="panel-title">02- SELECT LOAD</h2>
  <span class="label" style="left:14px;top:44px">Qty</span>
  <span class="label" style="left:131px;top:44px">Stack</span>
  <span class="label" style="left:186px;top:44px">Load</span>
  <span class="label" style="left:350px;top:44px">Weight</span>
  <span class="label" style="left:459px;top:44px">Unit</span>
  <div class="field" style="left:15px;top:64px;width:96px">05<svg class="ctl" width="7" height="12" viewBox="0 0 7 12"><path d="M1 4l2.5-3 2.5 3M1 8l2.5 3 2.5-3" stroke="#fff" stroke-width="1.4" fill="none"/></svg></div>
  <div class="check" style="left:140px;top:74px"><svg width="18" height="20" viewBox="0 0 18 20"><path d="M3 11l4 5 9-14" stroke="var(--tick)" stroke-width="2.5" fill="none"/></svg></div>
  <div class="field" style="left:186px;top:64px;width:147px">Box / Pallet<svg class="ctl" width="8" height="5" viewBox="0 0 8 5"><path d="M1 1l3 3 3-3" stroke="#fff" stroke-width="1.5" fill="none"/></svg></div>
  <div class="field" style="left:347px;top:64px;width:96px">100<svg class="ctl" width="7" height="12" viewBox="0 0 7 12"><path d="M1 4l2.5-3 2.5 3M1 8l2.5 3 2.5-3" stroke="#fff" stroke-width="1.4" fill="none"/></svg></div>
  <div class="field" style="left:458px;top:64px;width:96px">kg<svg class="ctl" width="8" height="5" viewBox="0 0 8 5"><path d="M1 1l3 3 3-3" stroke="#fff" stroke-width="1.5" fill="none"/></svg></div>

  <span class="label" style="left:15px;top:112px">Lenght</span>
  <span class="label" style="left:122px;top:112px">Width</span>
  <span class="label" style="left:228px;top:112px">Height</span>
  <span class="label" style="left:333px;top:112px">Unit</span>
  <span class="label" style="left:439px;top:112px">Add Units</span>
  <div class="field" style="left:15px;top:131px;width:96px">105<svg class="ctl" width="7" height="12" viewBox="0 0 7 12"><path d="M1 4l2.5-3 2.5 3M1 8l2.5 3 2.5-3" stroke="#fff" stroke-width="1.4" fill="none"/></svg></div>
  <div class="field" style="left:121px;top:131px;width:96px">105<svg class="ctl" width="7" height="12" viewBox="0 0 7 12"><path d="M1 4l2.5-3 2.5 3M1 8l2.5 3 2.5-3" stroke="#fff" stroke-width="1.4" fill="none"/></svg></div>
  <div class="field" style="left:227px;top:131px;width:96px">105<svg class="ctl" width="7" height="12" viewBox="0 0 7 12"><path d="M1 4l2.5-3 2.5 3M1 8l2.5 3 2.5-3" stroke="#fff" stroke-width="1.4" fill="none"/></svg></div>
  <div class="field" style="left:333px;top:131px;width:96px">cm<svg class="ctl" width="8" height="5" viewBox="0 0 8 5"><path d="M1 1l3 3 3-3" stroke="#fff" stroke-width="1.5" fill="none"/></svg></div>
  <div class="field center" style="left:439px;top:131px;width:115px">More Units</div>
</section>

<section class="abs panel" style="left:171px;top:412px;width:278px;height:180px">
  <h2 class="panel-title">03- TOTAL LOAD</h2>
  <span class="label" style="left:14px;top:64px">Total</span>
  <span class="label" style="left:14px;top:103px">CBM</span>
  <span class="label" style="left:14px;top:143px">KG</span>
  <div class="field center" style="left:58px;top:52px;width:206px">05</div>
  <div class="field center" style="left:58px;top:91px;width:206px">03</div>
  <div class="field center" style="left:58px;top:131px;width:206px">100</div>
</section>

<section class="abs panel" style="left:460px;top:412px;width:277px;height:180px">
  <h2 class="panel-title">04- SELECT LOCATION</h2>
  <span class="label" style="left:13px;top:64px">From</span>
  <span class="label" style="left:14px;top:143px">To</span>
  <div class="field center" style="left:57px;top:52px;width:206px">Shipping Area Or Port</div>
  <svg class="abs" style="left:152px;top:100px" width="18" height="22" viewBox="0 0 18 22"><path d="M6 0h6v12h5l-8 9-8-9h5z" fill="#5aaae8"/></svg>
  <div class="field center" style="left:57px;top:131px;width:206px">Shipping Area Or Port</div>
</section>

<section class="abs panel" style="left:750px;top:412px;width:279px;height:180px">
  <h2 class="panel-title">05- SELECT OPTIONS</h2>
  <div class="check" style="left:19px;top:47px"><svg width="18" height="20" viewBox="0 0 18 20"><path d="M3 11l4 5 9-14" stroke="var(--tick)" stroke-width="2.5" fill="none"/></svg></div>
  <span class="opt" style="left:46px;top:49px">IMPORT</span>
  <div class="check" style="left:19px;top:79px"></div>
  <span class="opt" style="left:50px;top:81px">EXPORT</span>
  <span class="opt" style="left:18px;top:111px">INCOTERM : <span style="color:#bfe0f8">FCA</span></span>

  <div class="check" style="left:172px;top:47px"><svg width="18" height="20" viewBox="0 0 18 20"><path d="M3 11l4 5 9-14" stroke="var(--tick)" stroke-width="2.5" fill="none"/></svg></div>
  <svg class="abs" style="left:205px;top:48px" width="12" height="14" viewBox="0 0 12 14"><path d="M6 0l6 2v5c0 3.5-3 6-6 7-3-1-6-3.5-6-7V2z" fill="#5aaae8"/></svg>
  <span class="opt" style="left:231px;top:50px">SAFE</span>
  <div class="check" style="left:172px;top:77px"><svg width="18" height="20" viewBox="0 0 18 20"><path d="M3 11l4 5 9-14" stroke="var(--tick)" stroke-width="2.5" fill="none"/></svg></div>
  <svg class="abs" style="left:204px;top:78px" width="14" height="14" viewBox="0 0 14 14"><path d="M4 13V8a3 3 0 0 1 6 0v5z M2 13h10" fill="#5aaae8" stroke="#5aaae8"/><path d="M7 1v2M2 3l1.5 1.5M12 3l-1.5 1.5" stroke="#5aaae8" stroke-width="1.2"/></svg>
  <span class="opt" style="left:223px;top:80px">ALERT</span>
  <div class="check" style="left:172px;top:107px"><svg width="18" height="20" viewBox="0 0 18 20"><path d="M3 11l4 5 9-14" stroke="var(--tick)" stroke-width="2.5" fill="none"/></svg></div>
  <svg class="abs" style="left:205px;top:108px" width="12" height="14" viewBox="0 0 12 14"><circle cx="6" cy="4" r="3.5" fill="#5aaae8"/><path d="M0 14c0-4 2.5-6 6-6s6 2 6 6z" fill="#5aaae8"/></svg>
  <span class="opt" style="left:221px;top:110px">GAURD</span>
  <div class="field center" style="left:17px;top:133px;width:245px;font-size:13px">PRICE LEVEL</div>
</section>

<div class="abs panel search-bar">SEARCH FOR QUOTES</div>
<p class="abs manual">or manualy !</p>

<div class="abs cranes" role="img" aria-label="Silhouettes of harbour cranes lifting containers along the quay"></div>
<footer class="abs footer"></footer>
<p class="abs copyright">Copyright © Cargoline Hub. All Right Reserved.</p>
<span class="abs social" style="left:921px" aria-label="Social link"></span>
<span class="abs social" style="left:949px" aria-label="Social link"></span>
<span class="abs social" style="left:981px" aria-label="Social link"></span>
<span class="abs social" style="left:1013px" aria-label="Social link"></span>

</body>
</html>
```